Banners for a bowtie/tie Fashion shop

I need banners (770x100) for a necktie and bowtie shop (http://www.kelorin.dk)

5 BOWTIE BANNERS:

I need the 3 text versions for eatch bowtie banner:

Danmarks største udvalg af butterfly
Køb butterfly. FRI fragt og FRI retur
Butterfly fra 199,- inkl. FRI fragt

5 NECKTIE BANNERS:

I need the 3 text versions for eatch necktie banner:

Danmarks største udvalg af slips
Køb slips. FRI fragt og FRI retur
Slips fra 199,- inkl. FRI fragt

All banners should contain the logo. All in JPG format and Photoshop/Inddesign/illustrator format

Target Market(s)

Guys and Gays

Industry/Entity Type

Shop

Requirements
Must have
• Logo
Nice to have
• Nice new pictures

```html
<!DOCTYPE html>
<html lang="da">
<head>
<meta charset="utf-8">
<title>Kelorin – butterfly banner</title>
<link rel="stylesheet" href="https://fonts.googleapis.com/css2?family=Open+Sans:wght@400;600&display=swap">
<style>
  :root {
    --navy: #0f1f5c;
    --sky: #2fa7df;
    --white: #ffffff;
    --ink: #2a2a2a;
    --blazer: #2c4c8c;
    --blazer-dark: #1c335f;
    --shirt: #a9c7e4;
  }
  html, body {
    margin: 0;
    padding: 0;
    overflow: hidden;
    background: var(--white);
  }
  .banner {
    position: relative;
    width: 1200px;
    height: 156px;
    overflow: hidden;
    background: var(--white);
    font-family: "Open Sans", Arial, sans-serif;
  }
  .headline {
    position: absolute;
    left: 16px;
    top: 16px;
    width: 540px;
    height: 54px;
    background: var(--navy);
    color: var(--white);
    font-size: 31px;
    font-weight: 400;
    line-height: 54px;
    padding-left: 10px;
    box-sizing: border-box;
    white-space: nowrap;
    z-index: 2;
  }
  .product-tag {
    position: absolute;
    left: 402px;
    top: 86px;
    width: 209px;
    height: 57px;
    background: var(--sky);
    color: var(--white);
    font-size: 44px;
    font-weight: 400;
    line-height: 54px;
    text-align: center;
    z-index: 2;
  }
  .brand-name {
    position: absolute;
    left: 18px;
    top: 102px;
    color: var(--ink);
    font-size: 30px;
    font-weight: 400;
    letter-spacing: -0.5px;
    line-height: 1;
    z-index: 2;
  }
  .model-photo {
    position: absolute;
    right: 0;
    top: 0;
    width: 480px;
    height: 156px;
    background:
      linear-gradient(90deg, var(--white) 0%, rgba(255,255,255,0) 22%),
      linear-gradient(90deg, var(--blazer-dark) 20%, var(--blazer) 45%, var(--shirt) 62%, var(--shirt) 80%, var(--blazer) 92%, var(--blazer-dark) 100%);
  }
</style>
</head>
<body>
  <div class="banner">
    <div class="model-photo" role="img" aria-label="Man in blue blazer and light blue shirt wearing a patterned red bowtie"></div>
    <div class="headline">Danmarks største udvalg af</div>
    <div class="brand-name">kelorin</div>
    <div class="product-tag">butterfly</div>
  </div>
</body>
</html>
```